Tilwa Sandrim Construction
Business Cards, Note Pads, Envelopes, Letterhead , signboard etc.
Bright & Fun-filled
Hamdan R. Al-Qutami
CEO
P.O Box 40573
Al-Hassa 36417
Saudi Arabia
Hamdan@tilwasandrim.com.sa
www.tilwasandrim.com.sa
Leave the back of the business card to write all the information in arabic
similar logo

```html
<!DOCTYPE html>
<html lang="en">
<head>
<meta charset="utf-8">
<title>Tilwa Sandrim Construction – Business Cards</title>
<link href="https://fonts.googleapis.com/css2?family=PT+Sans:wght@400;700&display=swap" rel="stylesheet">
<style>
  :root {
    --stage: #dcdcdc;
    --card-white: #ffffff;
    --brand-red: #c4161c;
    --deep-red: #8e0d12;
    --ink: #333333;
    --swoosh-grey: #b9b9b9;
    --night: #120204;
  }
  * { box-sizing: border-box; margin: 0; padding: 0; }
  html, body { width: 1200px; height: 777px; overflow: hidden; }
  body {
    background: var(--stage);
    font-family: "PT Sans", Arial, sans-serif;
    position: relative;
  }
  .card {
    position: absolute;
    border-radius: 22px;
    overflow: hidden;
    box-shadow: 0 4px 10px rgba(0,0,0,0.25);
  }
  .card-front { left: 336px; top: 101px; width: 792px; height: 302px; background: var(--card-white); }
  .card-back-light { left: 58px; top: 432px; width: 518px; height: 293px; background: var(--card-white); }
  .card-back-dark {
    left: 612px; top: 432px; width: 521px; height: 293px;
    background: radial-gradient(ellipse at 50% 40%, #d3161d 0%, var(--deep-red) 38%, #3a0407 70%, var(--night) 100%);
  }
  .swoosh { position: absolute; inset: 0; width: 100%; height: 100%; }

  .brand { position: absolute; display: flex; flex-direction: column; align-items: center; }
  .brand-dot { width: 54px; height: 54px; border-radius: 50%; background: var(--brand-red); margin-bottom: 12px; }
  .brand-name {
    font-weight: 700; color: var(--brand-red); text-align: center;
    font-size: 34px; line-height: 1.05; letter-spacing: 1px;
  }
  .card-front .brand { left: 24px; top: 40px; width: 230px; }
  .card-back-light .brand, .card-back-dark .brand { left: 0; right: 0; top: 58px; }
  .card-back-dark .brand-dot { background: #ffffff; }
  .card-back-dark .brand-name { color: #ffffff; }

  .identity { position: absolute; right: 149px; top: 26px; text-align: right; }
  .person-name { color: var(--brand-red); font-weight: 700; font-size: 27px; line-height: 1.1; }
  .person-role { color: var(--ink); font-size: 15px; margin-top: 2px; }
  .postal { position: absolute; right: 160px; top: 82px; text-align: right; color: var(--ink); font-size: 14px; line-height: 1.3; }

  .contacts { position: absolute; right: 40px; top: 136px; list-style: none; }
  .contacts li {
    display: flex; align-items: center; justify-content: flex-end; gap: 10px;
    color: #ffffff; font-size: 14px; height: 20.5px;
  }
  .contacts svg { width: 14px; height: 14px; fill: #ffffff; flex: none; }

  .site-url { position: absolute; left: 0; right: 0; bottom: 20px; text-align: center; font-size: 17px; color: var(--ink); }
  .site-url strong { color: var(--brand-red); }
  .card-back-dark .site-url { color: #ffffff; }
  .card-back-dark .site-url strong { color: #ff3a3f; }
</style>
</head>
<body>

<section class="card card-front">
  <svg class="swoosh" viewBox="0 0 792 302" preserveAspectRatio="none" aria-hidden="true">
    <path d="M0,190 C210,226 420,236 560,160 C650,114 720,98 792,94 L792,130 C720,134 650,150 560,196 C420,268 210,258 0,222 Z" fill="var(--swoosh-grey)"/>
    <path d="M0,210 C210,246 420,256 560,180 C650,134 720,118 792,114 L792,302 L0,302 Z" fill="var(--brand-red)"/>
  </svg>

  <div class="brand">
    <span class="brand-dot"></span>
    <span class="brand-name">TILWA SANDRIM</span>
  </div>

  <div class="identity">
    <p class="person-name">Hamdan R. Al-Qutami</p>
    <p class="person-role">CEO</p>
  </div>
  <div class="postal">
    <p>P.O Box 40573</p>
    <p>Al-Hassa 36417, Saudi Arabia</p>
  </div>

  <ul class="contacts">
    <li>+96613550142
      <svg viewBox="0 0 24 24"><path d="M6.6 10.8a15 15 0 0 0 6.6 6.6l2.2-2.2a1 1 0 0 1 1-.25 11 11 0 0 0 3.6.6 1 1 0 0 1 1 1V20a1 1 0 0 1-1 1A17 17 0 0 1 3 4a1 1 0 0 1 1-1h3.5a1 1 0 0 1 1 1c0 1.25.2 2.45.6 3.6a1 1 0 0 1-.25 1z"/></svg></li>
    <li>+966500718263
      <svg viewBox="0 0 24 24"><path d="M7 1h10a2 2 0 0 1 2 2v18a2 2 0 0 1-2 2H7a2 2 0 0 1-2-2V3a2 2 0 0 1 2-2zm0 4v13h10V5zm5 14.5a1 1 0 1 0 0 2 1 1 0 0 0 0-2z"/></svg></li>
    <li>+96613550187
      <svg viewBox="0 0 24 24"><path d="M6 3h9l3 3v4H6zm-2 8h16a2 2 0 0 1 2 2v6h-4v2H6v-2H2v-6a2 2 0 0 1 2-2zm4 5v3h8v-3z"/></svg></li>
    <li>Hamdan@tilwasandrim.com.sa
      <svg viewBox="0 0 24 24"><path d="M2 5h20v14H2zm2 2v.5l8 5 8-5V7zm0 3v7h16v-7l-8 5z"/></svg></li>
    <li>www.tilwasandrim.com.sa
      <svg viewBox="0 0 24 24"><circle cx="12" cy="12" r="10"/><path d="M2 12h20M12 2c3 3 3 17 0 20M12 2c-3 3-3 17 0 20" stroke="var(--brand-red)" stroke-width="1.5" fill="none"/></svg></li>
  </ul>
</section>

<section class="card card-back-light">
  <div class="brand">
    <span class="brand-dot"></span>
    <span class="brand-name">TILWA SANDRIM</span>
  </div>
  <p class="site-url">www.<strong>tilwasandrim</strong>.com.sa</p>
</section>

<section class="card card-back-dark">
  <div class="brand">
    <span class="brand-dot"></span>
    <span class="brand-name">TILWA SANDRIM</span>
  </div>
  <p class="site-url">www.<strong>tilwasandrim</strong>.com.sa</p>
</section>

</body>
</html>
```